Jubo Application for Cars Accidents Services

We need app screen designs for company provide services for the cars that got accidents, the design should be modern official and simple, the pages around 26 include login, register, auth code, home, splash, request service, profile, settings, booking, booking info ..., we need something so professional please.

Target Market(s)

Cars owners

```html
<!DOCTYPE html>
<html lang="en">
<head>
<meta charset="utf-8">
<title>Jubo – Sign in screens</title>
<link href="https://fonts.googleapis.com/css2?family=Quicksand:wght@500;600;700&family=Inter:wght@400;500;700&display=swap" rel="stylesheet">
<style>
  :root{
    --green:#3bb54a;
    --ink:#2c3440;
    --muted:#7c838c;
    --line:#d5d8dc;
    --kb-bg:#d1d4da;
    --key:#ffffff;
    --key-dark:#abb0ba;
    --photo-top:#6b6a68;
    --photo-mid:#8d9294;
    --photo-bottom:#3a3936;
    --white:#ffffff;
  }
  *{box-sizing:border-box;margin:0;padding:0}
  html,body{width:1200px;height:783px;overflow:hidden;background:var(--white)}
  .stage{position:relative;width:1200px;height:783px;overflow:hidden;background:var(--white)}
  .world{position:absolute;left:0;top:0;width:2048px;height:1336px;transform:scale(0.5859375);transform-origin:0 0}
  .screen{position:absolute;top:304px;width:375px;height:812px;overflow:hidden;background:var(--white);font-family:"Quicksand",sans-serif}
  .screen--login{left:249px}
  .screen--login-typing{left:656px}
  .screen--forgot{left:1063px}
  .screen--verify{left:1469px}

  .photo{position:absolute;inset:0;background:linear-gradient(180deg,var(--photo-top) 0%,#57585a 25%,var(--photo-mid) 55%,#5c5f61 75%,var(--photo-bottom) 100%)}
  .photo::after{content:"";position:absolute;inset:0;background:rgba(0,0,0,.18)}

  .status{position:absolute;left:0;top:0;width:375px;height:40px;font-family:"Inter",sans-serif;font-weight:700;font-size:12px}
  .status__time{position:absolute;left:20px;top:11px;color:#111}
  .status__icons{position:absolute;right:22px;top:12px}
  .screen--login .status__time,.screen--login-typing .status__time{color:#fff}

  .brand{position:absolute;left:97px;top:80px;width:180px;height:180px;border-radius:50%;background:var(--white);display:flex;align-items:center;justify-content:center}
  .brand__name{font-weight:700;font-size:32px;color:var(--ink);letter-spacing:1px}

  .field{position:absolute;left:15px;width:345px;height:30px;border-bottom:1px solid rgba(255,255,255,.8);color:#fff;font-size:15px;font-weight:700;letter-spacing:1px}
  .field--email{top:300px}
  .field--password{top:370px}
  .forgot-link{position:absolute;right:17px;top:424px;color:var(--green);font-size:14px;font-weight:600;letter-spacing:1px}
  .btn{position:absolute;left:14px;width:346px;height:56px;background:var(--green);color:#fff;font-size:15px;font-weight:700;letter-spacing:1px;display:flex;align-items:center;justify-content:center;border-radius:2px}
  .btn--login{top:469px}
  .btn--form{top:289px;box-shadow:0 3px 6px rgba(0,0,0,.2)}
  .signup{position:absolute;left:0;width:375px;top:556px;text-align:center;color:#fff;font-size:15px;font-weight:700;letter-spacing:1px}
  .signup span{color:var(--green)}
  .home-bar{position:absolute;left:121px;top:797px;width:134px;height:5px;border-radius:3px;background:#ddd}
  .home-bar--dark{background:#5d5f63}

  .title{position:absolute;left:0;width:375px;top:98px;text-align:center;font-size:23px;font-weight:600;color:var(--ink);letter-spacing:1.5px}
  .subtitle{position:absolute;left:0;width:375px;top:137px;text-align:center;font-size:15px;font-weight:500;color:var(--muted);letter-spacing:1.5px}
  .field--plain{top:222px;color:var(--muted);font-weight:500;border-bottom:1px solid var(--line);font-size:15px}
  .otp{position:absolute;top:198px;left:0;width:375px;height:30px;font-size:22px;font-weight:700;color:var(--ink)}
  .otp span{position:absolute}
  .otp i{position:absolute;top:11px;width:11px;height:11px;border-radius:50%;background:#8e9399}

  .keyboard{position:absolute;left:0;top:521px;width:375px;height:291px;background:var(--kb-bg);font-family:"Inter",sans-serif}
  .kb-row{position:absolute;left:0;width:375px;display:flex;justify-content:center;gap:6px}
  .key{height:42px;width:31.5px;background:var(--key);border-radius:5px;box-shadow:0 1px 0 #8a8e94;display:flex;align-items:center;justify-content:center;font-size:23px;color:#000}
  .key--fn{background:var(--key-dark);font-size:16px}
  .kb-row--1{top:8px}
  .kb-row--2{top:62px}
  .kb-row--3{top:116px}
  .kb-row--3 .key--fn{width:42px}
  .kb-row--3 .gap{width:8px}
  .kb-row--4{top:170px}
  .key--wide{width:87px;font-size:16px}
  .key--space{width:182px;font-size:16px}
  .kb-icon{position:absolute;top:237px}

  .numpad{position:absolute;left:0;top:521px;width:375px;height:291px;background:var(--kb-bg);font-family:"Inter",sans-serif}
  .numpad__grid{position:absolute;left:5px;top:7px;display:grid;grid-template-columns:repeat(3,118px);grid-auto-rows:51px;column-gap:6px;row-gap:6px}
  .nkey{background:var(--key);border-radius:5px;box-shadow:0 1px 0 #8a8e94;display:flex;flex-direction:column;align-items:center;justify-content:center;font-size:26px;line-height:1}
  .nkey small{font-size:10px;letter-spacing:1.5px;margin-top:2px}
  .nkey--blank{background:transparent;box-shadow:none}
</style>
</head>
<body>
<div class="stage">
  <div class="world">

    <section class="screen screen--login">
      <div class="photo" role="img" aria-label="Photo of a service car parked beside a building"></div>
      <div class="status">
        <span class="status__time">9:41 AM</span>
        <svg class="status__icons" width="64" height="12" viewBox="0 0 64 12"><g fill="#fff"><rect x="0" y="7" width="3" height="4"/><rect x="4" y="5" width="3" height="6"/><rect x="8" y="3" width="3" height="8"/><rect x="12" y="1" width="3" height="10"/><path d="M22 4a9 9 0 0 1 12 0l-1.5 1.5a7 7 0 0 0-9 0z M25 7a5 5 0 0 1 6 0L28 10z"/><rect x="40" y="2" width="20" height="9" rx="2" fill="none" stroke="#fff"/><rect x="42" y="4" width="15" height="5"/></g></svg>
      </div>
      <div class="brand"><span class="brand__name">Jubo</span></div>
      <div class="field field--email">Email</div>
      <div class="field field--password">Password</div>
      <div class="forgot-link">Forgot Password?</div>
      <div class="btn btn--login">Login</div>
      <p class="signup">New to Jubo? <span>Signup</span></p>
      <div class="home-bar"></div>
    </section>

    <section class="screen screen--login-typing">
      <div class="photo" role="img" aria-label="Photo of a service car parked beside a building"></div>
      <div class="status">
        <span class="status__time">9:41 AM</span>
        <svg class="status__icons" width="64" height="12" viewBox="0 0 64 12"><g fill="#fff"><rect x="0" y="7" width="3" height="4"/><rect x="4" y="5" width="3" height="6"/><rect x="8" y="3" width="3" height="8"/><rect x="12" y="1" width="3" height="10"/><path d="M22 4a9 9 0 0 1 12 0l-1.5 1.5a7 7 0 0 0-9 0z M25 7a5 5 0 0 1 6 0L28 10z"/><rect x="40" y="2" width="20" height="9" rx="2" fill="none" stroke="#fff"/><rect x="42" y="4" width="15" height="5"/></g></svg>
      </div>
      <div class="brand"><span class="brand__name">Jubo</span></div>
      <div class="field field--email">user@mailbox.com</div>
      <div class="field field--password">Password</div>
      <div class="forgot-link">Forgot Password?</div>
      <div class="btn btn--login">Login</div>
      <div class="keyboard">
        <div class="kb-row kb-row--1"><span class="key">Q</span><span class="key">W</span><span class="key">E</span><span class="key">R</span><span class="key">T</span><span class="key">Y</span><span class="key">U</span><span class="key">I</span><span class="key">O</span><span class="key">P</span></div>
        <div class="kb-row kb-row--2"><span class="key">A</span><span class="key">S</span><span class="key">D</span><span class="key">F</span><span class="key">G</span><span class="key">H</span><span class="key">J</span><span class="key">K</span><span class="key">L</span></div>
        <div class="kb-row kb-row--3"><span class="key key--fn">⬆</span><span class="gap"></span><span class="key">Z</span><span class="key">X</span><span class="key">C</span><span class="key">V</span><span class="key">B</span><span class="key">N</span><span class="key">M</span><span class="gap"></span><span class="key key--fn">⌫</span></div>
        <div class="kb-row kb-row--4"><span class="key key--fn key--wide">123</span><span class="key key--space">space</span><span class="key key--fn key--wide">return</span></div>
        <svg class="kb-icon" style="left:24px" width="28" height="28" viewBox="0 0 28 28"><circle cx="14" cy="14" r="12" fill="none" stroke="#555" stroke-width="1.6"/><circle cx="10" cy="11" r="1.5" fill="#555"/><circle cx="18" cy="11" r="1.5" fill="#555"/><path d="M8 16q6 6 12 0" fill="none" stroke="#555" stroke-width="1.6"/></svg>
        <svg class="kb-icon" style="left:330px" width="16" height="28" viewBox="0 0 16 28"><rect x="4" y="2" width="8" height="15" rx="4" fill="none" stroke="#555" stroke-width="1.6"/><path d="M1 13a7 7 0 0 0 14 0M8 20v6" fill="none" stroke="#555" stroke-width="1.6"/></svg>
        <div class="home-bar home-bar--dark" style="top:276px"></div>
      </div>
    </section>

    <section class="screen screen--forgot">
      <div class="status">
        <span class="status__time">9:41 AM</span>
        <svg class="status__icons" width="64" height="12" viewBox="0 0 64 12"><g fill="#333"><rect x="0" y="7" width="3" height="4"/><rect x="4" y="5" width="3" height="6"/><rect x="8" y="3" width="3" height="8"/><rect x="12" y="1" width="3" height="10"/><path d="M22 4a9 9 0 0 1 12 0l-1.5 1.5a7 7 0 0 0-9 0z M25 7a5 5 0 0 1 6 0L28 10z"/><rect x="40" y="2" width="20" height="9" rx="2" fill="none" stroke="#333"/><rect x="42" y="4" width="15" height="5"/></g></svg>
      </div>
      <h1 class="title">Forgot Password?</h1>
      <p class="subtitle">Retrieve Your Password</p>
      <div class="field field--plain">Email</div>
      <div class="btn btn--form">Submit</div>
      <div class="keyboard">
        <div class="kb-row kb-row--1"><span class="key">Q</span><span class="key">W</span><span class="key">E</span><span class="key">R</span><span class="key">T</span><span class="key">Y</span><span class="key">U</span><span class="key">I</span><span class="key">O</span><span class="key">P</span></div>
        <div class="kb-row kb-row--2"><span class="key">A</span><span class="key">S</span><span class="key">D</span><span class="key">F</span><span class="key">G</span><span class="key">H</span><span class="key">J</span><span class="key">K</span><span class="key">L</span></div>
        <div class="kb-row kb-row--3"><span class="key key--fn">⬆</span><span class="gap"></span><span class="key">Z</span><span class="key">X</span><span class="key">C</span><span class="key">V</span><span class="key">B</span><span class="key">N</span><span class="key">M</span><span class="gap"></span><span class="key key--fn">⌫</span></div>
        <div class="kb-row kb-row--4"><span class="key key--fn key--wide">123</span><span class="key key--space">space</span><span class="key key--fn key--wide">return</span></div>
        <svg class="kb-icon" style="left:24px" width="28" height="28" viewBox="0 0 28 28"><circle cx="14" cy="14" r="12" fill="none" stroke="#555" stroke-width="1.6"/><circle cx="10" cy="11" r="1.5" fill="#555"/><circle cx="18" cy="11" r="1.5" fill="#555"/><path d="M8 16q6 6 12 0" fill="none" stroke="#555" stroke-width="1.6"/></svg>
        <svg class="kb-icon" style="left:330px" width="16" height="28" viewBox="0 0 16 28"><rect x="4" y="2" width="8" height="15" rx="4" fill="none" stroke="#555" stroke-width="1.6"/><path d="M1 13a7 7 0 0 0 14 0M8 20v6" fill="none" stroke="#555" stroke-width="1.6"/></svg>
        <div class="home-bar home-bar--dark" style="top:276px"></div>
      </div>
    </section>

    <section class="screen screen--verify">
      <div class="status">
        <span class="status__time">9:41 AM</span>
        <svg class="status__icons" width="64" height="12" viewBox="0 0 64 12"><g fill="#333"><rect x="0" y="7" width="3" height="4"/><rect x="4" y="5" width="3" height="6"/><rect x="8" y="3" width="3" height="8"/><rect x="12" y="1" width="3" height="10"/><path d="M22 4a9 9 0 0 1 12 0l-1.5 1.5a7 7 0 0 0-9 0z M25 7a5 5 0 0 1 6 0L28 10z"/><rect x="40" y="2" width="20" height="9" rx="2" fill="none" stroke="#333"/><rect x="42" y="4" width="15" height="5"/></g></svg>
      </div>
      <h1 class="title">Verify your Mobile</h1>
      <p class="subtitle">Enter your OTP code here</p>
      <div class="otp"><span style="left:98px">8</span><span style="left:156px">6</span><i style="left:208px"></i><i style="left:260px"></i></div>
      <div class="btn btn--form">Verify Now</div>
      <div class="numpad">
        <div class="numpad__grid">
          <span class="nkey">1<small>&nbsp;</small></span>
          <span class="nkey">2<small>ABC</small></span>
          <span class="nkey">3<small>DEF</small></span>
          <span class="nkey">4<small>GHI</small></span>
          <span class="nkey">5<small>JKL</small></span>
          <span class="nkey">6<small>MNO</small></span>
          <span class="nkey">7<small>PQRS</small></span>
          <span class="nkey">8<small>TUV</small></span>
          <span class="nkey">9<small>WXYZ</small></span>
          <span class="nkey nkey--blank"></span>
          <span class="nkey">0</span>
          <span class="nkey nkey--blank"><svg width="26" height="18" viewBox="0 0 26 18"><path d="M8 1h16v16H8L1 9z" fill="none" stroke="#333" stroke-width="1.4"/><path d="M12 5l8 8M20 5l-8 8" stroke="#333" stroke-width="1.4"/></svg></span>
        </div>
        <div class="home-bar home-bar--dark" style="top:276px"></div>
      </div>
    </section>

  </div>
</div>
</body>
</html>
```